Harlune Painting

Need business card design

Target Market(s)

Paint

Industry/Entity Type

Painting

Requirements
Must have
• Brice Halvorn | Superviser
| HarLune Painting
| mobile: (360) 555-0148
| email: Brice@harluneinc.example
| site: www.harluneinc.example
| address: 718 Corliss Rd NE Ste 300, Olympia, WA 98501

```html
<!DOCTYPE html>
<html lang="en">
<head>
<meta charset="utf-8">
<title>Harlune Painting – Business Card</title>
<link rel="stylesheet" href="https://fonts.googleapis.com/css2?family=Crimson+Pro:ital,wght@0,600;1,400&display=swap">
<style>
  :root {
    --card-bg: #ffffff;
    --brand-navy: #1e3d86;
    --brand-green: #62bf24;
  }
  html, body {
    margin: 0;
    padding: 0;
    width: 1200px;
    height: 720px;
    overflow: hidden;
    background: var(--card-bg);
  }
  .card {
    position: relative;
    width: 1200px;
    height: 720px;
    background: var(--card-bg);
    font-family: "Crimson Pro", Georgia, serif;
    color: var(--brand-navy);
  }
  .brand-name {
    position: absolute;
    top: 262px;
    left: 0;
    width: 100%;
    margin: 0;
    text-align: center;
    font-weight: 600;
    font-size: 62px;
    line-height: 1;
    letter-spacing: 1px;
    color: var(--brand-navy);
  }
  .contact-person {
    position: absolute;
    top: 452px;
    left: 0;
    width: 100%;
    text-align: center;
  }
  .person-name {
    margin: 0;
    font-weight: 600;
    font-size: 50px;
    line-height: 1.05;
    letter-spacing: 0.5px;
  }
  .person-title {
    margin: 0;
    font-style: italic;
    font-weight: 400;
    font-size: 38px;
    line-height: 1.1;
    letter-spacing: 2px;
  }
</style>
</head>
<body>
  <main class="card">
    <p class="brand-name">Harlune Painting</p>
    <section class="contact-person">
      <h1 class="person-name">Brice Halvorn</h1>
      <p class="person-title">Supervisor</p>
    </section>
  </main>
</body>
</html>
```